Lunaform website scandinavian interior design

Existing website: http://lunaform-example.no/

Webdesign for interior designer Ragna Tveitmo. The company name is Lunaform. Scandinavian interiør is known to be simple and elegant. The website will be in Norwegian, we are working on the text. The website needs to have a few more pages than just the front page. Here are the different titles of the pages:

1. Hjem
2. Om Lunaform
3. Tjenester og priser
4.. Kontakt oss

There should be Chatterloop and Pixelane icons somewhere at the bottom of the website.

The logo we want to use is attached (pink with black print, see attachment )

We have attached images for inspiration. We want to use some of these colors. The color in the logo, The style should be elegant, modern and delicate.

It is imprtant that the website is user friendly.

Target Market(s)

People who want to decorate their home
Companies and public sector who need to redecorate

Industry/Entity Type

Interior Designer

Coding

Coded - Design and coding required

Number of Pages Required

5+ page

Font styles to use
Other font styles liked:
• see example in the logo breakdown

Requirements
Must have
• Elegant, modern and delicate design
Images of design, see examples attached
Colors similar to the pictures
Should not have
• Too bright colors
Pictures of people

```html
<!DOCTYPE html>
<html lang="no">
<head>
<meta charset="utf-8">
<title>Lunaform – Farge &amp; interiørdesign</title>
<link href="https://fonts.googleapis.com/css2?family=Jost:wght@400;500;600;700&family=Cormorant+Garamond:ital,wght@0,400;1,400&display=swap" rel="stylesheet">
<style>
  :root{
    --ink:#221412;
    --text:#1b1b1b;
    --blush:#f2dcd8;
    --white:#ffffff;
    --card-shadow:rgba(0,0,0,0.12);
    --muted:#5a5a5a;
  }
  *{box-sizing:border-box;margin:0;padding:0}
  html,body{width:1200px;height:3020px;overflow:hidden;background:var(--white)}
  body{position:relative;font-family:"Jost",sans-serif;color:var(--text)}
  .abs{position:absolute}

  /* hero */
  .brand{left:88px;top:30px;font-family:"Jost",sans-serif;font-size:30px;font-weight:400;color:var(--ink);letter-spacing:1px}
  .brand-sub{left:90px;top:72px;font-size:8px;letter-spacing:2px;color:var(--ink)}
  .hero-title{left:88px;top:212px;width:320px;font-size:26px;font-weight:500;line-height:33px;text-transform:uppercase;color:var(--ink)}
  .hero-copy{left:88px;top:320px;width:300px;font-size:14.5px;line-height:20px}
  .btn{display:flex;align-items:center;justify-content:center;width:191px;height:42px;background:var(--ink);color:var(--white);font-size:17px;box-shadow:0 2px 3px var(--card-shadow)}
  .hero-btn{left:88px;top:482px}
  .social{display:flex;align-items:center;gap:7px;font-size:15px;color:var(--ink)}
  .social i{display:block;width:14px;height:14px;background:var(--ink);border-radius:2px}
  .hero-photo{left:422px;top:0;width:398px;height:674px;background:linear-gradient(160deg,#f4f4f2 0%,#e3e4e1 45%,#c9cbc6 75%,#b8ad9d 100%)}
  .panel-blush{left:820px;top:0;width:380px;height:337px;background:var(--blush)}
  .panel-ink{left:820px;top:337px;width:380px;height:337px;background:var(--ink)}
  .panel-text{left:75px;width:280px;font-size:26px;line-height:33px}
  .menu{left:1086px;top:34px}

  /* intro */
  .lines{left:88px;top:783px}
  .intro{left:88px;top:850px;width:1030px;font-size:19px;line-height:25px}
  .intro p+p{margin-top:25px}
  .intro-btn{left:88px;top:1068px}

  /* section headings */
  .sec-title{left:0;width:1200px;text-align:center;font-size:19.5px;font-weight:700;letter-spacing:.5px}
  .sec-title::after{content:"";display:block;width:58px;height:2px;background:var(--ink);margin:6px auto 0}
  .sec-sub{left:0;width:1200px;text-align:center;font-size:19px;line-height:25px;text-transform:uppercase}

  /* services */
  .card{top:1294px;width:356px;height:350px;background:var(--white);box-shadow:0 2px 5px var(--card-shadow);text-align:center}
  .card-photo{height:177px}
  .card h3{margin-top:18px;font-size:20px;font-weight:700;letter-spacing:.5px}
  .card p{margin:14px auto 0;width:300px;font-size:14.5px;line-height:20px}
  .more{display:inline-flex;align-items:center;gap:6px;font-size:18px;text-transform:uppercase}
  .card .more{margin-top:10px}

  /* products */
  .product{background:linear-gradient(180deg,#fafafa,#ececec)}
  .arrow-btn{top:2218px}
  .prod-more{left:0;width:1200px;top:2291px;text-align:center}

  /* social */
  .tile{top:2529px;width:248px;height:249px}

  /* footer */
  .footer{left:0;top:2889px;width:1200px;height:131px;background:var(--blush)}
  .nav{position:absolute;top:20px;font-size:16.5px;text-transform:uppercase;transform:translateX(-50%);white-space:nowrap}
  .copy{position:absolute;left:0;top:100px;width:1200px;text-align:center;font-size:14px;text-transform:uppercase}
</style>
</head>
<body>

<!-- hero -->
<div class="abs brand">Lunaform</div>
<div class="abs brand-sub">FARGE &amp; INTERIØRDESIGN</div>
<h1 class="abs hero-title">Trenger du hjelp til utvikling av interiørmiljøer?</h1>
<p class="abs hero-copy">Lorem ipsum dolor sit amet, consetetur sadipscing elitr, sed diam nonumy eirmod tempor invidunt ut labore et dolore magna aliquyam erat, sed diam voluptua. At vero eos et accusam et justo duo dolores et ea rebum. Stet clita kasd gubergren, no sea takimata sanctus.</p>
<a class="abs btn hero-btn">Kontakt oss</a>
<div class="abs social" style="left:88px;top:611px"><i></i>Pixelane</div>
<div class="abs social" style="left:88px;top:642px"><i></i>Chatterloop</div>

<div class="abs hero-photo" role="img" aria-label="Lys skandinavisk stue og kjøkken med hvite vegger, pendellamper og lys sofa"></div>

<div class="abs panel-blush">
  <svg class="abs menu" width="30" height="22" viewBox="0 0 30 22"><g stroke="#221412" stroke-width="2"><line x1="0" y1="2" x2="30" y2="2"/><line x1="0" y1="11" x2="30" y2="11"/><line x1="0" y1="20" x2="30" y2="20"/></g></svg>
  <div class="abs panel-text" style="top:134px;color:var(--ink)">Skal du pusse opp i hjemmet ditt? <svg width="28" height="16" viewBox="0 0 28 16"><path d="M1 8h25M19 1l7 7-7 7" fill="none" stroke="#221412" stroke-width="2"/></svg></div>
</div>
<div class="abs panel-ink">
  <div class="abs panel-text" style="top:120px;color:var(--white)">Trenger du hjelp til utvikling av interiørmiljøer? <svg width="28" height="16" viewBox="0 0 28 16"><path d="M1 8h25M19 1l7 7-7 7" fill="none" stroke="#fff" stroke-width="2"/></svg></div>
</div>

<!-- intro -->
<svg class="abs lines" width="62" height="26" viewBox="0 0 62 26"><g stroke="#221412" stroke-width="2"><line x1="0" y1="1" x2="62" y2="1"/><line x1="0" y1="9" x2="48" y2="9"/><line x1="0" y1="17" x2="36" y2="17"/><line x1="0" y1="25" x2="22" y2="25"/></g></svg>
<div class="abs intro">
  <p>Firma Lunaform AS&nbsp; jobber med utvikling av interiørmiljøer for private, bedrifter og offentlige institusjoner. For å finne de optimale løsninger til et prosjekt, enten det er et rom eller fler, kreves det kjennskap og kunnskap i markedet. Ved å bruke profesjonell kompetanse på området, sparer du både tid og penger.<br>Bruk av plantegninger/møbleringsplaner, 3D tegninger, Collager eller «lage en levende collage» – så finner vi de beste løsninger for deg som kunde.</p>
  <p>Målet er alltid kunden i fokus – få det som du/dere vil ha det.</p>
</div>
<a class="abs btn intro-btn">Learn More</a>

<!-- services -->
<h2 class="abs sec-title" style="top:1221px">OUR SERVICES</h2>
<div class="abs card" style="left:214px">
  <div class="card-photo" role="img" aria-label="Moderne kjøkken med lyse fronter og spisebord" style="background:linear-gradient(120deg,#3a3a3a 0%,#d8d4cf 40%,#c9b29a 70%,#9a9a98 100%)"></div>
  <h3>PRIVATE INTERIØR</h3>
  <p>Lorem ipsum dolor sit amet, consetetur sadipscing elitr, sed diam nonumy eirmod tempor invidunt ut labore et dolore magna</p>
  <a class="more">Learn more <svg width="18" height="12" viewBox="0 0 18 12"><path d="M1 6h15M11 1l5 5-5 5" fill="none" stroke="#1b1b1b" stroke-width="1.6"/></svg></a>
</div>
<div class="abs card" style="left:629px">
  <div class="card-photo" role="img" aria-label="Møterom med lyst trebord og grå stoler" style="background:linear-gradient(150deg,#e8e6e2 0%,#d9c6ad 50%,#b7b8ba 100%)"></div>
  <h3>BEDRIFT/OFFENTLIG</h3>
  <p>Lorem ipsum dolor sit amet, consetetur sadipscing elitr, sed diam nonumy eirmod tempor invidunt ut labore et dolore magna</p>
  <a class="more">Learn more <svg width="18" height="12" viewBox="0 0 18 12"><path d="M1 6h15M11 1l5 5-5 5" fill="none" stroke="#1b1b1b" stroke-width="1.6"/></svg></a>
</div>

<!-- products -->
<h2 class="abs sec-title" style="top:1756px">FEATURED PRODUCTS</h2>
<div class="abs sec-sub" style="top:1838px">Lorem ipsum dolor sit amet,<br>consetetur sadipscing elitr, sed.</div>
<div class="abs product" role="img" aria-label="Hvit gulvlampe" style="left:41px;top:1940px;width:147px;height:240px;background:linear-gradient(180deg,#fbfbfb,#efefef)"></div>
<div class="abs product" role="img" aria-label="Barkrakk i lys eik" style="left:463px;top:1922px;width:228px;height:340px;background:linear-gradient(180deg,#e4c9a4,#c99b67)"></div>
<div class="abs product" role="img" aria-label="Hvit barstol" style="left:990px;top:1946px;width:153px;height:234px;background:linear-gradient(180deg,#f6f5f3,#e9e7e4)"></div>
<svg class="abs arrow-btn" style="left:242px" width="46" height="46" viewBox="0 0 46 46"><circle cx="23" cy="23" r="22" fill="none" stroke="#1b1b1b" stroke-width="1.5"/><path d="M33 23H13M20 16l-7 7 7 7" fill="none" stroke="#1b1b1b" stroke-width="1.8"/></svg>
<svg class="abs arrow-btn" style="left:912px" width="46" height="46" viewBox="0 0 46 46"><circle cx="23" cy="23" r="22" fill="none" stroke="#1b1b1b" stroke-width="1.5"/><path d="M13 23h20M26 16l7 7-7 7" fill="none" stroke="#1b1b1b" stroke-width="1.8"/></svg>
<div class="abs prod-more"><a class="more">Learn more <svg width="18" height="12" viewBox="0 0 18 12"><path d="M1 6h15M11 1l5 5-5 5" fill="none" stroke="#1b1b1b" stroke-width="1.6"/></svg></a></div>

<!-- social -->
<h2 class="abs sec-title" style="top:2426px">LETS GET SOCIAL</h2>
<div class="abs sec-sub" style="top:2486px;font-size:17px">Latest Pixelane posts</div>
<div class="abs tile" role="img" aria-label="Stue med skjenk, vaser og tre" style="left:88px;background:linear-gradient(160deg,#cfc6ba,#8a7560 70%,#2f3b4a)"></div>
<div class="abs tile" role="img" aria-label="Spisestue med trebord og bilder på veggen" style="left:346px;background:linear-gradient(160deg,#f0efed,#cfc9c2 60%,#8a6e55)"></div>
<div class="abs tile" role="img" aria-label="Lyst spisebord med svart pendellampe" style="left:605px;background:linear-gradient(160deg,#f2efe9,#dcd6cc 60%,#5a5753)"></div>
<div class="abs tile" role="img" aria-label="Spisegruppe foran stort kunstverk i rust og beige" style="left:864px;background:linear-gradient(160deg,#b9a897,#a36d4c 50%,#d7c7b5)"></div>

<!-- footer -->
<footer class="abs footer">
  <a class="nav" style="left:195px">Hjem</a>
  <a class="nav" style="left:409px">Om Lunaform</a>
  <a class="nav" style="left:687px">Tjenester og priser</a>
  <a class="nav" style="left:969px">Kontakt oss</a>
  <div class="abs social" style="left:175px;top:82px"><i></i>Chatterloop</div>
  <div class="abs social" style="left:976px;top:82px"><i></i>Pixelane</div>
  <div class="copy">2020@ All rights reserved - Lunaform</div>
</footer>

</body>
</html>
```